Webdesign plus CSS for a German company data register

We need a unique and attractive webdesign including CSS development for a website (https://kontorfeld.de/) of our newly founded company. We collect company data from several public registers to display them aggregated.

Your design should communicate science, data security, a business note and perhaps a slice of nerdness. Elements - like color and layout - of our logo should also be found in your design.

Target Market(s)

banks, insurance companies, authorities etc.

Industry/Entity Type

Internet

Coding

Coded - Design and coding required

Number of Pages Required

3 page

Font styles to use
Sans Serif

Requirements
Must have
• mockups, CSS

eye catching, easy to read / navigate
Nice to have
• pictogramms / logos for essential content

```html
<!DOCTYPE html>
<html lang="de">
<head>
<meta charset="utf-8">
<title>Kontorfeld – Start</title>
<link rel="stylesheet" href="https://fonts.googleapis.com/css2?family=Open+Sans:wght@400;600;700&display=swap">
<style>
:root{
  --orange:#ff5000;
  --dark:#4f4f4f;
  --text:#444;
  --grey:#8c8c8c;
  --band:#ededed;
  --blue:#1f6fa8;
  --cyan:#29abe2;
  --line:#c8c8c8;
}
*{margin:0;padding:0;box-sizing:border-box}
html,body{width:960px;height:1200px;overflow:hidden;background:#fff;font-family:"Open Sans",sans-serif;color:var(--text)}
.page{position:relative;width:960px;height:1200px}
.abs{position:absolute}
.header{position:absolute;left:0;top:0;width:960px;height:36px;background:#fff;box-shadow:0 1px 3px rgba(0,0,0,.18)}
.header-corner{position:absolute;left:0;top:0}
.brand{position:absolute;left:126px;top:10px;font-size:11px;font-weight:700;color:var(--orange);letter-spacing:.3px}
.nav{position:absolute;top:11px;font-size:9px;font-weight:600;letter-spacing:.8px;color:var(--dark)}
.nav.active{border-bottom:1.5px solid var(--orange);padding:0 4px 3px}
.btn{position:absolute;background:var(--orange);color:#fff;display:flex;align-items:center;justify-content:center;box-shadow:0 1px 3px rgba(0,0,0,.25)}
.lang{position:absolute;left:872px;top:11px;font-size:9px;color:var(--dark);font-weight:600}
.lang::after{content:"";display:inline-block;margin-left:4px;border:3px solid transparent;border-top:3.5px solid var(--dark);vertical-align:-1px}
.hero-title{position:absolute;width:960px;text-align:center;color:var(--dark);font-weight:600}
.hero-brand span:first-child{color:var(--orange)}
.hero-brand span:last-child{color:var(--grey)}
.question{left:352px;top:275px;width:255px;height:60px;font-size:12.5px;font-weight:600;letter-spacing:.4px}
.tree{position:absolute;background:var(--line)}
.choice{position:absolute;top:403px;width:120px;height:120px;background:#fff;box-shadow:0 1px 4px rgba(0,0,0,.15)}
.choice svg{position:absolute;left:41px;top:16px}
.choice .btn{left:25px;top:81px;width:70px;height:22px;font-size:8px;font-weight:700;letter-spacing:.4px}
.values{position:absolute;left:0;top:610px;width:960px;height:190px;background:var(--band);border:1px solid #7fc6e4}
.value-icon{position:absolute;top:20px}
.value-text{position:absolute;top:100px;width:188px;height:65px;background:#fff;box-shadow:0 1px 3px rgba(0,0,0,.15);font-size:8.3px;line-height:1.15;padding:0 15px 0 17px;display:flex;align-items:center;color:var(--dark)}
.notes{position:absolute;left:306px;top:881px;font-size:8.3px;color:var(--dark);list-style:none}
.notes li{position:relative;padding-left:12px;margin-bottom:11px;line-height:1.15;width:340px}
.notes li::before{content:"";position:absolute;left:0;top:3px;width:4px;height:4px;border-radius:50%;background:var(--dark)}
.hint{position:absolute;left:319px;top:944px;font-size:8.3px;color:var(--dark)}
.privacy-band{position:absolute;left:1px;top:1030px;width:959px;height:37px;background:var(--dark);color:#fff;font-size:8.5px;font-weight:700;letter-spacing:.8px;display:flex;align-items:center;justify-content:center}
.privacy-band a{color:var(--orange);margin-left:8px;text-decoration:none}
.footer{position:absolute;top:1174px;font-size:8.3px}
.footer a{color:var(--orange);text-decoration:none}
</style>
</head>
<body>
<div class="page">

  <header class="header">
    <svg class="header-corner" width="96" height="36" viewBox="0 0 96 36">
      <polygon points="0,0 34,0 66,36 0,36" fill="var(--orange)"/>
      <polygon points="34,0 62,0 94,36 66,36" fill="var(--dark)"/>
    </svg>
    <div class="brand">Kontorfeld</div>
    <div class="nav active" style="left:531px">Start</div>
    <div class="nav" style="left:575px">Firmen</div>
    <div class="nav" style="left:627px">Personen</div>
    <div class="nav" style="left:691px">Statistiken</div>
    <div class="btn" style="left:765px;top:7px;width:70px;height:22px;font-size:9.5px">Kontakt</div>
    <div class="lang">DE</div>
  </header>

  <h1 class="hero-title" style="top:99px;font-size:22px;letter-spacing:1px">Willkommen</h1>
  <div class="hero-title" style="top:144px;font-size:17px">zu</div>
  <div class="hero-title hero-brand" style="top:176px;font-size:26px;letter-spacing:1px"><span>Kontor</span><span>feld</span></div>

  <div class="btn question">Was möchten Sie suchen?</div>
  <div class="tree" style="left:479px;top:335px;width:1px;height:33px"></div>
  <div class="tree" style="left:340px;top:368px;width:280px;height:1px"></div>
  <div class="tree" style="left:340px;top:368px;width:1px;height:35px"></div>
  <div class="tree" style="left:619px;top:368px;width:1px;height:35px"></div>

  <div class="choice" style="left:278px">
    <svg width="38" height="40" viewBox="0 0 38 40" aria-hidden="true">
      <rect x="7" y="1" width="24" height="38" fill="none" stroke="var(--dark)" stroke-width="1.2"/>
      <rect x="1" y="16" width="14" height="23" fill="#fff" stroke="var(--dark)" stroke-width="1.2"/>
      <g fill="none" stroke="var(--cyan)" stroke-width="1">
        <rect x="4" y="20" width="3" height="3"/><rect x="9" y="20" width="3" height="3"/>
        <rect x="4" y="26" width="3" height="3"/><rect x="9" y="26" width="3" height="3"/>
        <rect x="4" y="32" width="3" height="3"/><rect x="9" y="32" width="3" height="3"/>
      </g>
      <g fill="none" stroke="var(--dark)" stroke-width="1">
        <rect x="12" y="5" width="3" height="3"/><rect x="18" y="5" width="3" height="3"/><rect x="24" y="5" width="3" height="3"/>
        <rect x="18" y="11" width="3" height="3"/><rect x="24" y="11" width="3" height="3"/>
        <rect x="18" y="18" width="3" height="3"/><rect x="24" y="18" width="3" height="3"/>
        <rect x="18" y="25" width="3" height="3"/><rect x="24" y="25" width="3" height="3"/>
        <rect x="24" y="32" width="3" height="3"/>
      </g>
    </svg>
    <div class="btn">Firmen</div>
  </div>

  <div class="choice" style="left:560px">
    <svg width="40" height="40" viewBox="0 0 40 40" aria-hidden="true">
      <circle cx="20" cy="20" r="18.5" fill="none" stroke="var(--cyan)" stroke-width="1.3"/>
      <circle cx="20" cy="16" r="6" fill="none" stroke="var(--dark)" stroke-width="1.1"/>
      <path d="M9 31c2-6 6-8 11-8s9 2 11 8" fill="none" stroke="var(--dark)" stroke-width="1.1"/>
    </svg>
    <div class="btn" style="left:27px">Personen</div>
  </div>

  <section class="values">
    <svg class="value-icon" style="left:179px" width="64" height="64" viewBox="0 0 64 64" aria-hidden="true">
      <circle cx="32" cy="32" r="30" fill="none" stroke="var(--orange)" stroke-width="1.6" stroke-dasharray="5 3"/>
      <g fill="none" stroke="var(--blue)" stroke-width="1.3">
        <rect x="17" y="18" width="30" height="19"/>
        <line x1="32" y1="15" x2="32" y2="18"/>
        <path d="M30 37l-5 10M34 37l5 10M32 37v10"/>
        <circle cx="26" cy="28" r="4.5"/>
        <path d="M26 28v-4.5M26 28h4.5"/>
        <path d="M33 24h9M33 28h9M33 32h9"/>
      </g>
    </svg>
    <svg class="value-icon" style="left:448px" width="64" height="64" viewBox="0 0 64 64" aria-hidden="true">
      <circle cx="32" cy="32" r="30" fill="none" stroke="var(--orange)" stroke-width="1.6" stroke-dasharray="5 3"/>
      <g fill="none" stroke="var(--blue)" stroke-width="1.6">
        <rect x="26" y="17" width="12" height="7"/>
        <path d="M32 24v6M20 30h24M20 30v7M32 30v7M44 30v7"/>
        <rect x="16" y="37" width="8" height="6"/>
        <rect x="28" y="37" width="8" height="6"/>
        <rect x="40" y="37" width="8" height="6"/>
      </g>
    </svg>
    <svg class="value-icon" style="left:717px" width="64" height="64" viewBox="0 0 64 64" aria-hidden="true">
      <circle cx="32" cy="32" r="30" fill="none" stroke="var(--orange)" stroke-width="1.6" stroke-dasharray="5 3"/>
      <g fill="none" stroke="var(--blue)" stroke-width="2">
        <path d="M19 18v26h27"/>
        <path d="M20 38l8-8 6 5 10-12"/>
        <path d="M38 22h7v7"/>
      </g>
      <line x1="33" y1="18" x2="33" y2="44" stroke="#9bb9d0" stroke-width="1"/>
    </svg>

    <p class="value-text" style="left:117px">Wir haben es uns zum Ziel gemacht ein seriöser Anbieter korrekter Handesl­regis­terdaten, Unternehmensdaten und Per­sonendaten zu werden</p>
    <p class="value-text" style="left:386px">Unsere Bestrebungen sind ehrliche und unmanipulierte Daten über Personen, Unternehmen, Firmen und Vereine</p>
    <p class="value-text" style="left:655px">Unser Ziel ist eine absolut transparente, ehrliche und faire Veröffentlichung</p>
  </section>

  <ul class="notes">
    <li>Sofern Sie einen fehlerhaften Eintrag finden würden wir uns über Ihr Feedback freuen</li>
    <li>Sofern Sie Ihren eigenen Eintrag verbessern oder ergänzen wollen, sind Sie herzlich eingeladen dies zu tun</li>
  </ul>
  <p class="hint">Nutzen Sie in beiden Fällen bitte unser Kontaktformular</p>
  <div class="btn" style="left:428px;top:971px;width:70px;height:22px;font-size:9.5px">Kontakt</div>

  <div class="privacy-band">Datenschutz steht bei uns an erster Stelle. sehen <a href="#">Datenschutz</a></div>

  <div class="footer" style="left:331px">© 2020 - Kontorfeld</div>
  <div class="footer" style="left:517px"><a href="#">Impressum</a></div>
  <div class="footer" style="left:586px"><a href="#">Datenschutz</a></div>

</div>
</body>
</html>
```